Ridgely Forge business card for handing simple contact information and generating service awareness

Utilizing the attached logo(s), generate a professional, but approachable, card conveying a sense of capability and integrity. Please only use one logo of the four attached; the different colors are all acceptable, but preference will be given to a design integrating a teal/turquoise logo,

I do not know where to put in the contact information or details?

Target Market(s)

Agriculture, Farming, Timber, Forestry, Construction, Crane Service

Industry/Entity Type

Contact Information for Business Card

Name, Phone Number, email address

Colors

Designer to choose colors to be used in the design.

Requirements
Nice to have
• It would be great to have either a mountain or one of the attached cranes as a backdrop on the rear of the card. Simple watermarks and/or Debossing is also great

```html
<!DOCTYPE html>
<html lang="en">
<head>
<meta charset="UTF-8">
<title>Ridgely Forge – Business Card</title>
<link href="https://fonts.googleapis.com/css2?family=Archivo:wght@400;700&display=swap" rel="stylesheet">
<style>
  :root {
    --teal: #2d6e63;
    --teal-deep: #255c53;
    --teal-light: #5aa597;
    --paper: #ffffff;
    --backdrop: #e6e6e4;
    --grey: #8a8a8a;
  }
  * { box-sizing: border-box; margin: 0; padding: 0; }
  html, body { width: 1200px; height: 802px; overflow: hidden; }
  body {
    background: var(--backdrop);
    font-family: "Archivo", Arial, sans-serif;
    position: relative;
  }
  .card {
    position: absolute;
    width: 525px;
    height: 300px;
    top: 251px;
    border-radius: 4px;
    overflow: hidden;
    box-shadow: 0 6px 18px rgba(0,0,0,.12);
  }
  /* Front */
  .card-front { left: 50px; background: var(--paper); }
  .front-band {
    position: absolute; left: 0; right: 0; bottom: 0; height: 132px;
    background: var(--teal);
  }
  .front-scene {
    position: absolute; right: 0; top: 70px; width: 190px; height: 230px;
    background: linear-gradient(160deg, var(--teal) 0%, var(--teal-deep) 60%, var(--teal-light) 100%);
    border-radius: 60px 0 0 0;
  }
  .holder { position: absolute; right: 24px; top: 14px; text-align: right; }
  .holder-name { color: var(--teal); font-weight: 700; font-size: 21px; line-height: 1.2; }
  .holder-role { color: var(--grey); font-size: 13px; margin-top: 2px; }
  .brand-mark {
    position: absolute; left: 30px; top: 100px;
    display: flex; align-items: center; gap: 12px;
  }
  .brand-dot { width: 26px; height: 26px; border-radius: 50%; background: var(--teal); }
  .brand-name { color: var(--teal); font-weight: 700; font-size: 26px; }
  .contact {
    position: absolute; left: 30px; bottom: 20px;
    color: var(--paper); font-size: 15px; line-height: 1.45;
  }
  .contact-line { display: flex; align-items: center; gap: 8px; }
  .contact-line svg { width: 13px; height: 13px; flex: none; }
  .services { margin-top: 6px; }
  /* Back */
  .card-back { left: 625px; background: var(--teal); }
  .back-title {
    position: absolute; left: 0; right: 0; top: 62px; text-align: center;
    color: var(--paper); font-weight: 700; font-size: 32px;
  }
  .back-scene {
    position: absolute; left: 40px; top: 150px; width: 250px; height: 250px;
    border-radius: 50%;
    background: radial-gradient(circle at 55% 60%, var(--teal-light) 0%, var(--teal) 70%);
    opacity: .55;
  }
</style>
</head>
<body>
  <section class="card card-front">
    <div class="front-band"></div>
    <div class="front-scene" role="img" aria-label="Illustration of mountains, pine forest and a tractor"></div>

    <div class="holder">
      <p class="holder-name">Dale Hutchins</p>
      <p class="holder-role">Owner / Operator</p>
    </div>

    <div class="brand-mark">
      <span class="brand-dot"></span>
      <span class="brand-name">Ridgely Forge</span>
    </div>

    <div class="contact">
      <p class="contact-line">
        <svg viewBox="0 0 16 16" fill="none" stroke="currentColor" stroke-width="1.6"><path d="M4 1.5 6 5 4.5 6.5c1 2 3 4 5 5L11 10l3.5 2-1 2.5C8 14 2 8 1.5 2.5Z"/></svg>
        (503) 555-0142
      </p>
      <p class="contact-line">
        <svg viewBox="0 0 16 16" fill="none" stroke="currentColor" stroke-width="1.6"><rect x="1.5" y="3" width="13" height="10" rx="1"/><path d="m1.5 3.5 6.5 5 6.5-5"/></svg>
        ridgelyforge@fieldmail.com
      </p>
      <div class="services">
        <p>Knuckleboom Lift Services</p>
        <p>Medium Duty Hauling and Transport</p>
      </div>
    </div>
  </section>

  <section class="card card-back">
    <div class="back-scene" role="img" aria-label="Debossed mountain, forest and tractor scene"></div>
    <h1 class="back-title">Ridgely Forge</h1>
  </section>
</body>
</html>
```